Values Statement poster template

We want to develop a poster template for our company policies and statements which promote our company values in our workplaces.
These documents are important in showing our clients, suppliers and employees who we are and what we stand for.
The graphic design will incorporate our company logo, and be bright, uplifting and inspiring, developing a graphic theme that we can utilise for other company documents. The design will graphically illustrate and support our values statement, with colour and modern design.
This values poster will be the first in a series of documents using the same theme.The format will be a4 and a3 portrait
We are an environmental service business specialising in rehabilitation and revegetation

Target Market(s)

Tier one clients in industry, Mining, Construction and agriculture

Font styles to use
Other font styles liked:
• calibri

Requirements
Must have
• Professional , high end feel, able to read clearly on a poster
Nice to have
• graphic design elements, symbols, etc which support the message, that can be carried through to various documents such as quality, environmental, safety policies
A bright theme which ties in with our logo colours.

```html
<!DOCTYPE html>
<html lang="en">
<head>
<meta charset="utf-8">
<title>Our Values Poster</title>
<link rel="stylesheet" href="https://fonts.googleapis.com/css2?family=Arimo:wght@400;700&family=Bebas+Neue&display=swap">
<style>
  :root {
    --page-bg: #e7e9ea;
    --poster-bg: #f2f3f2;
    --forest: #0f7040;
    --forest-soft: #2f8446;
    --leaf: #1b7a3d;
    --fresh: #4fa646;
    --mint: #d7ead3;
    --orange: #ee7a30;
    --ink: #2d2d2d;
    --white: #ffffff;
  }
  * { box-sizing: border-box; margin: 0; padding: 0; }
  html, body {
    width: 1200px; height: 1021px; overflow: hidden;
    background: var(--page-bg);
    font-family: "Arimo", Arial, sans-serif;
    color: var(--ink);
  }
  .poster-frame {
    position: absolute; left: 243px; top: 10px;
    width: 713px; height: 1000px;
  }
  .poster {
    position: absolute; left: 0; top: 0;
    width: 873px; height: 1224px;
    transform: scale(0.817); transform-origin: 0 0;
    background: var(--poster-bg);
    overflow: hidden;
    box-shadow: 0 6px 24px rgba(0,0,0,0.12);
  }
  .hero-shape, .footer-band { position: absolute; left: 0; }
  .hero-shape { top: 0; }
  .footer-band { top: 1160px; }
  .hero-decoration {
    position: absolute; left: 320px; top: 40px; width: 92px; height: 150px;
    background: var(--forest-soft); opacity: 0.8;
  }
  .hero-title {
    position: absolute; left: 62px; top: 48px;
    font-family: "Bebas Neue", "Oswald", sans-serif;
    font-size: 96px; line-height: 85px; color: var(--white);
    letter-spacing: 1px;
  }
  .brand {
    position: absolute; left: 515px; top: 66px;
    display: flex; align-items: center; gap: 12px;
  }
  .brand-dot { width: 34px; height: 34px; border-radius: 50%; background: var(--fresh); }
  .brand-name { font-weight: 700; font-size: 40px; color: var(--forest); }
  .brand-rule {
    position: absolute; left: 454px; top: 155px; width: 430px; height: 2px;
    background: var(--leaf);
  }
  .brand-rule::before {
    content: ""; position: absolute; left: -3px; top: -2px;
    width: 6px; height: 6px; border-radius: 50%; background: var(--leaf);
  }
  .tagline {
    position: absolute; left: 60px; top: 362px;
    border-left: 4px solid var(--orange);
    padding: 2px 0 2px 21px;
    font-size: 21px; line-height: 28.5px; color: var(--leaf);
    text-transform: uppercase;
  }
  .value { position: absolute; width: 370px; font-size: 12px; line-height: 18.5px; }
  .value-head { display: flex; align-items: center; margin-bottom: 16px; }
  .value-icon { flex: none; background: var(--mint); border-radius: 40%; }
  .value-title {
    font-weight: 700; font-size: 16.5px; line-height: 20.5px; color: var(--leaf);
    text-transform: uppercase;
  }
  .value-sub { font-size: 14.5px; color: var(--leaf); margin-top: 3px; }
  .value p { margin-bottom: 6px; }
  .value ul { list-style: none; }
  .value li { position: relative; padding-left: 11px; }
  .value li::before { content: "•"; position: absolute; left: 0; font-size: 10px; }

  .v-people   { left: 60px;  top: 544px; }
  .v-planet   { left: 60px;  top: 792px; }
  .v-standard { left: 60px;  top: 962px; }
  .v-safe     { left: 452px; top: 202px; }
  .v-proud    { left: 452px; top: 552px; }
  .v-succeed  { left: 452px; top: 774px; }
  .v-give     { left: 452px; top: 1062px; }
</style>
</head>
<body>
  <div class="poster-frame">
    <main class="poster">
      <svg class="hero-shape" width="430" height="315" viewBox="0 0 430 315" aria-hidden="true">
        <circle cx="150" cy="35" r="275" fill="var(--forest)"/>
      </svg>
      <div class="hero-decoration" role="img" aria-label="Leaf artwork area"></div>
      <h1 class="hero-title">Our<br>Values</h1>

      <div class="brand">
        <span class="brand-dot"></span>
        <span class="brand-name">Verdanta</span>
      </div>
      <div class="brand-rule"></div>

      <p class="tagline">These are the things<br>we value most,<br>they define the way<br>we do business</p>

      <section class="value v-people">
        <div class="value-head">
          <div class="value-icon" role="img" aria-label="Illustration of a team of people" style="width:88px;height:70px;margin-right:20px"></div>
          <div>
            <h2 class="value-title">We value our people</h2>
            <div class="value-sub">above everything else.</div>
          </div>
        </div>
        <p>We demonstrate this by:</p>
        <ul>
          <li>Providing safe, positive, enjoyable workplaces where everyone feels valued and respected</li>
          <li>Providing Careers, not Jobs, we grow together</li>
          <li>Encouraging inclusion, participation and collaboration</li>
          <li>Recognising and rewarding contribution and excellence</li>
          <li>Supporting our people through tough times</li>
        </ul>
      </section>

      <section class="value v-planet">
        <div class="value-head">
          <div class="value-icon" role="img" aria-label="Illustration of a seedling growing from soil" style="width:70px;height:75px;margin-right:20px"></div>
          <div>
            <h2 class="value-title">We do good things</h2>
            <div class="value-sub">for the planet</div>
          </div>
        </div>
        <p>Our products are helping revegetate Australia, which we are tremendously proud of.<br>We minimise our environmental impact in everything we do.</p>
      </section>

      <section class="value v-standard">
        <div class="value-head">
          <div class="value-icon" role="img" aria-label="Illustration of an award rosette" style="width:66px;height:72px;margin-right:20px"></div>
          <h2 class="value-title">We set the<br>standard</h2>
        </div>
        <ul>
          <li>We are uncompromising on quality</li>
          <li>We are the best at what we do, and we do what we are best at</li>
          <li>We are always improving</li>
          <li>We are pioneering</li>
        </ul>
      </section>

      <section class="value v-safe">
        <div class="value-head">
          <div class="value-icon" role="img" aria-label="Illustration of a safety shield with a tick" style="width:56px;height:66px;margin-right:30px"></div>
          <h2 class="value-title">Our workplaces<br>are safe</h2>
        </div>
        <p>There is nothing more important to us than our people going home healthy and safe every day. We won’t accept anything less. We believe safety is a management choice. By providing safe work systems, and education we achieve our daily goal of Zero Harm. At Verdanta we;</p>
        <ul>
          <li>Take the time to make our work areas safe, whatever it takes</li>
          <li>Don’t accept shortcuts</li>
          <li>Look out for each other</li>
          <li>Investigate our incidents and learn from them, we won’t accept repeats</li>
          <li>Are constantly looking for ways to improve the safety of our workplaces.</li>
          <li>Think safe, work safer, go home safe!</li>
        </ul>
      </section>

      <section class="value v-proud">
        <div class="value-head">
          <div class="value-icon" role="img" aria-label="Illustration of raised hands" style="width:72px;height:72px;margin-right:20px"></div>
          <h2 class="value-title">We are proud of<br>who we are</h2>
        </div>
        <p>Our reputation means the world to us. We:</p>
        <ul>
          <li>Treat everyone with respect and we expect it in return</li>
          <li>Follow the rules</li>
          <li>Do what we say we will do</li>
          <li>Own our mistakes and we fix them</li>
          <li>Are trustworthy and transparent</li>
        </ul>
      </section>

      <section class="value v-succeed">
        <div class="value-head">
          <div class="value-icon" role="img" aria-label="Illustration of steps leading to a flag" style="width:72px;height:70px;margin-right:24px"></div>
          <h2 class="value-title">We succeed<br>together</h2>
        </div>
        <p>We believe in win-win relationships. When our business is profitable everyone benefits, our owners, employees, clients and the community. At Verdanta we:</p>
        <ul>
          <li>Work as a team, we get it done together</li>
          <li>We treat our suppliers and subcontractors like they are part of the team.</li>
          <li>Are building on our success, and growing together</li>
          <li>Choose to work with employees, customers and suppliers who fit our values</li>
        </ul>
      </section>

      <section class="value v-give">
        <div class="value-head">
          <div class="value-icon" role="img" aria-label="Illustration of a hand holding a heart" style="width:72px;height:68px;margin-right:20px"></div>
          <h2 class="value-title">We give back</h2>
        </div>
        <p>We appreciate our success and we give back by supporting our community, and those less fortunate.</p>
      </section>

      <svg class="footer-band" width="873" height="64" viewBox="0 0 873 64" aria-hidden="true">
        <defs>
          <linearGradient id="band-fill" x1="0" x2="1" y1="0" y2="0">
            <stop offset="0" stop-color="var(--fresh)"/>
            <stop offset="0.55" stop-color="#2f8d3f"/>
            <stop offset="1" stop-color="var(--forest)"/>
          </linearGradient>
        </defs>
        <path d="M0 6 H408 Q418 6 418 16 V38 Q418 46 428 46 H873 V64 H0 Z" fill="url(#band-fill)"/>
      </svg>
    </main>
  </div>
</body>
</html>
```